On-the-go, individually packaged flushable wipe packaging

Design the front and back of an individually packaged flushable wipe product.

The package is 4 inches tall and 2 inches wide. There are only two sides to the package, front and back. It is constructed of two sheets of printed, foil-lined plastic that are heat welded together.

The front should be decorative and playful and have space for a logo / product name on it (no logo has been created yet so use your imagination if you wish). It should be unisex and envoke somewhat outdoorsy vibes that would appeal to mountain bikers, marathon runners, travelers, and adventurers of all kinds. It can draw attention to itself through color but not through potty humor or bathroom references. People should be able to take these to work or send them with their children to school with being embarrassed.

Important note: Similar to business cards, the packaging material is printed and then cut in a grid. The machine that cuts the packaging may be off by a couple millimeters so any artwork or colors that extend to the sides of the packaging should continue onto the opposite side of the next package like a tesselation or book-matched wood, left side should match up to right side and top should match up to bottom.

The back should contain the follow information (iconography and layout up to you):

- Contains one hygienic towelette
- (Key selling points)
- Flushable & Biodegradable
- 100% natural fibers
- Gentle cleansing formula
- No parabens or fragrances
- (For use on…)
- Hands
- Face*
- Body
- Nether areas
- Messy surfaces
- *Avoid eyes/forehead before sweating and scruff (snags fibers)
- Please care for our planet, cities, and sewer systems by recycling this packaging after use. Do not flush packaging.

```html
<!DOCTYPE html>
<html lang="en">
<head>
<meta charset="utf-8">
<title>Roamly — Flushable Wet Wipe Pouch, Front and Back</title>
<link rel="stylesheet" href="https://fonts.googleapis.com/css2?family=Lexend:wght@400;500;600;700;800&family=Anton&display=swap">
<style>
  :root {
    --leaf-green: #4bb36b;
    --leaf-green-light: #55bb75;
    --sky: #66c6f0;
    --sky-light: #8fd4f5;
    --sky-pale: #a6ddf7;
    --navy: #0d57a5;
    --ink-blue: #1670c0;
    --white: #ffffff;
    --paper: #ffffff;
  }
  * { box-sizing: border-box; margin: 0; padding: 0; }
  html, body { width: 1200px; height: 952px; overflow: hidden; background: var(--paper); }
  body { position: relative; font-family: "Lexend", sans-serif; }

  .pouch { position: absolute; overflow: hidden; box-shadow: 0 6px 14px rgba(0,0,0,0.12); }
  .pouch--front { left: 183px; top: 73px; width: 405px; height: 789px; background: var(--sky); }
  .pouch--back  { left: 651px; top: 75px; width: 402px; height: 786px; background: var(--sky); }

  .seal-band { position: absolute; left: 0; top: 0; width: 100%; height: 37px; background: var(--leaf-green); }

  .fill-panel {
    position: absolute; border-radius: 4px;
    background: linear-gradient(180deg, var(--sky-pale) 0%, var(--sky-light) 25%, var(--sky) 100%);
    box-shadow: inset 0 0 6px rgba(255,255,255,0.45);
  }
  .pouch--front .fill-panel { left: 30px; top: 37px; width: 344px; height: 715px; }
  .pouch--back .fill-panel  { left: 27px; top: 36px; width: 343px; height: 714px; }

  .product-line { position: absolute; left: 97px; top: 80px; color: var(--white);
    font-weight: 600; font-size: 17px; letter-spacing: 3px; line-height: 20px; text-align: right; }
  .pack-count { position: absolute; left: 250px; top: 78px; color: var(--ink-blue);
    font-weight: 300; font-size: 42px; line-height: 42px; }

  .brand-box { position: absolute; left: 70px; top: 148px; width: 265px; height: 260px; background: var(--white);
    display: flex; align-items: center; justify-content: center; padding-bottom: 40px; }
  .brand-name { color: var(--navy); font-weight: 800; font-size: 56px; letter-spacing: -1px; }

  .wave { position: absolute; left: 0; top: 370px; width: 405px; height: 419px; }

  .benefits { position: absolute; left: 70px; top: 428px; width: 320px; list-style: none; }
  .benefit { position: absolute; left: 0; display: flex; align-items: center; }
  .benefit__icon { width: 60px; height: 50px; border-radius: 50%; background: rgba(255,255,255,0.22); }
  .benefit__text { position: absolute; left: 84px; color: var(--white); font-weight: 600;
    font-size: 17px; letter-spacing: 1.4px; line-height: 20.5px; white-space: nowrap; }
  .benefit--gentle  { top: 0; }
  .benefit--gentle .benefit__text { top: -8px; }
  .benefit--natural { top: 87px; }
  .benefit--natural .benefit__text { top: 3px; }
  .benefit--clean   { top: 160px; }
  .benefit--clean .benefit__text { top: 3px; }

  .scent-tag { position: absolute; left: 108px; top: 671px; width: 173px; height: 27px; border-radius: 14px;
    background: var(--white); color: var(--navy); font-weight: 500; font-size: 15px; letter-spacing: 4px;
    display: flex; align-items: center; justify-content: center; }

  .use-box { position: absolute; left: 55px; top: 141px; width: 292px; height: 225px;
    border: 1.5px solid var(--ink-blue); border-radius: 6px; }
  .use-box__title { position: absolute; top: 26px; width: 100%; text-align: center; color: var(--ink-blue);
    font-weight: 600; font-size: 19px; letter-spacing: 0.5px; }
  .use-item { position: absolute; display: flex; gap: 8px; color: var(--ink-blue); font-weight: 700;
    font-size: 19px; line-height: 20px; }
  .use-item svg { flex: none; width: 15px; height: 15px; margin-top: 3px; }
  .use-item--hands   { left: 22px;  top: 64px; }
  .use-item--face    { left: 22px;  top: 96px; }
  .use-item--body    { left: 22px;  top: 129px; }
  .use-item--nether  { left: 139px; top: 64px; }
  .use-item--messy   { left: 139px; top: 111px; }
  .use-box__note { position: absolute; left: 21px; top: 167px; color: var(--ink-blue);
    font-size: 12.5px; line-height: 17px; }

  .claim-badge { position: absolute; left: 71px; top: 399px; width: 272px; height: 79px; }
  .claim-badge__frame { position: absolute; left: 0; top: 0; }
  .claim-badge__pct { position: absolute; left: 2px; top: 0; font-family: "Anton", sans-serif;
    font-size: 42px; line-height: 46px; color: var(--navy); letter-spacing: -1px; }
  .claim-badge__line1 { position: absolute; left: 111px; top: 10px; font-family: "Anton", sans-serif;
    font-size: 27px; line-height: 30px; color: var(--white); letter-spacing: 0.5px; }
  .claim-badge__line2 { position: absolute; left: 9px; top: 40px; font-family: "Anton", sans-serif;
    font-size: 27px; line-height: 32px; color: var(--white); letter-spacing: 0.5px; }

  .copy { position: absolute; left: 66px; width: 290px; color: var(--ink-blue); font-size: 16px; line-height: 20px; }
  .copy--directions { top: 502px; }
  .copy--planet { top: 561px; }
</style>
</head>
<body>

<section class="pouch pouch--front" aria-label="Pouch front">
  <div class="fill-panel"></div>
  <div class="seal-band"></div>
  <p class="product-line">FLUSHABLE<br>WET WIPE</p>
  <p class="pack-count">X1</p>
  <div class="brand-box"><span class="brand-name">Roamly</span></div>
  <svg class="wave" viewBox="0 0 405 419" preserveAspectRatio="none" aria-hidden="true">
    <path d="M0 31 C60 5 110 0 170 12 C240 25 300 50 405 28 L405 419 L0 419 Z" fill="var(--leaf-green)"/>
    <rect x="30" y="40" width="344" height="342" fill="var(--leaf-green-light)" opacity="0.35" rx="4"/>
  </svg>
  <ul class="benefits">
    <li class="benefit benefit--gentle"><span class="benefit__icon" role="img" aria-label="Water drop icon"></span><span class="benefit__text">GENTLE<br>CLEANSING<br>FORMULA</span></li>
    <li class="benefit benefit--natural"><span class="benefit__icon" role="img" aria-label="Plant leaves icon"></span><span class="benefit__text">100% NATURAL<br>FIBERS</span></li>
    <li class="benefit benefit--clean"><span class="benefit__icon" role="img" aria-label="Leaf over hand icon"></span><span class="benefit__text">NO PARABENS<br>OR FRAGRANCES</span></li>
  </ul>
  <div class="scent-tag">UNSCENTED</div>
</section>

<section class="pouch pouch--back" aria-label="Pouch back">
  <div class="fill-panel"></div>
  <div class="use-box">
    <p class="use-box__title">FOR USE ON:</p>
    <div class="use-item use-item--hands"><svg viewBox="0 0 16 16"><rect x="1" y="2" width="12" height="12" fill="none" stroke="currentColor" stroke-width="1.4"/><path d="M4 8l3 3 7-9" fill="none" stroke="currentColor" stroke-width="1.6"/></svg><span>HANDS</span></div>
    <div class="use-item use-item--face"><svg viewBox="0 0 16 16"><rect x="1" y="2" width="12" height="12" fill="none" stroke="currentColor" stroke-width="1.4"/><path d="M4 8l3 3 7-9" fill="none" stroke="currentColor" stroke-width="1.6"/></svg><span>FACE*</span></div>
    <div class="use-item use-item--body"><svg viewBox="0 0 16 16"><rect x="1" y="2" width="12" height="12" fill="none" stroke="currentColor" stroke-width="1.4"/><path d="M4 8l3 3 7-9" fill="none" stroke="currentColor" stroke-width="1.6"/></svg><span>BODY</span></div>
    <div class="use-item use-item--nether"><svg viewBox="0 0 16 16"><rect x="1" y="2" width="12" height="12" fill="none" stroke="currentColor" stroke-width="1.4"/><path d="M4 8l3 3 7-9" fill="none" stroke="currentColor" stroke-width="1.6"/></svg><span>NETHER<br>AREAS</span></div>
    <div class="use-item use-item--messy"><svg viewBox="0 0 16 16"><rect x="1" y="2" width="12" height="12" fill="none" stroke="currentColor" stroke-width="1.4"/><path d="M4 8l3 3 7-9" fill="none" stroke="currentColor" stroke-width="1.6"/></svg><span>MESSY<br>SURFACES</span></div>
    <p class="use-box__note">*Avoid eyes/forehead before<br>sweating and scruff (snags fibers)</p>
  </div>

  <div class="claim-badge">
    <svg class="claim-badge__frame" width="272" height="79" viewBox="0 0 272 79" aria-hidden="true">
      <path d="M110 1 H262 Q271 1 271 10 V69 Q271 78 262 78 H22" fill="none" stroke="var(--sky-pale)" stroke-width="1.5"/>
    </svg>
    <span class="claim-badge__pct">100%</span>
    <span class="claim-badge__line1">FLUSHABLE</span>
    <span class="claim-badge__line2">&amp; BIODEGRADABLE</span>
  </div>

  <p class="copy copy--directions">DIRECTIONS: Tear open, unfold wipe, use and flush.</p>
  <p class="copy copy--planet">Please care for our planet, cities, and sewer systems by recycling this packaging after use. Do not flush packaging.</p>
</section>

</body>
</html>
```